Redesign digital storytelling app interface for picking topics and recording/listening to audio

We are building an app for users to tell stories to their friends and family in response to prompts. Our current interface is very basic, and we want to have it redesigned in order to make it more visually appealing and feel more like a comfortable conversation. We also need one screen created from scratch to match the existing screens.
In this app, the user picks a story topic from a list a friend has sent to them and then makes an audio recording in response to that topic. The other user receives the recording and listens to it, then responds to the story.
Attached are images of the screens we want to have redesigned.
1. Topic Selection Screen - screen showing the three prompts that the user will pick from before recording their story.
2. Story Recording Screen - screen that the user sees while recording their story.
3. Playback Screen - screen that the user sees while listening to the story.
4. Respond to Story Screen - screen that the user sees after listening to the story on the playback screen. This screen should have buttons for the user to communicate with the person who sent them the story, including: a quick record button where the user can send a voice message responding to the story, a phone call button, a text button, a velnorix button, and a drumo button. It should also have a button to return to the main menu.
I've also attached a graphic showing what we are currently using for a logo and color scheme. This does not need to be followed exactly.
As an added bonus, please give an example of how to manage these screens when the stories are not one-on-one, but in a group of four people.
The mood of this product should be comfortable, personal, and conversational. We want people to feel like they're chatting with an old friend. The design itself can be anything at all, so go wild!
Digital

```html
<!DOCTYPE html>
<html lang="en">
<head>
<meta charset="utf-8">
<title>Tell a Story – Pick a Topic</title>
<link rel="stylesheet" href="https://fonts.googleapis.com/css2?family=Tinos&family=Marcellus&display=swap">
<style>
  :root {
    --bg-center: #474747;
    --bg-edge: #1f1f1f;
    --green-light: #5fae34;
    --green-dark: #3c861d;
    --green-text: #4e8d2b;
    --green-edge: #4f9a2a;
    --tag-bg: #6b6c6e;
    --card-bg: #363636;
    --text-light: #e4e4e4;
    --text-white: #ffffff;
    --topic-center: #43603a;
    --topic-edge: #1e1f1e;
  }
  * { margin: 0; padding: 0; box-sizing: border-box; }
  html, body { width: 675px; height: 1200px; overflow: hidden; background: var(--bg-edge); }
  .screen {
    position: relative;
    width: 675px; height: 1200px; overflow: hidden;
    background: radial-gradient(ellipse 70% 55% at 50% 45%, var(--bg-center), var(--bg-edge));
    font-family: "Marcellus", sans-serif;
  }
  .app-header { position: absolute; left: 0; top: 0; width: 675px; height: 150px; }
  .app-header svg { position: absolute; inset: 0; filter: drop-shadow(0 6px 8px rgba(0,0,0,.55)); }
  .app-logo {
    position: absolute; left: 0; right: 0; top: 40px;
    text-align: center; font-family: "Tinos", serif; font-size: 46px;
    color: var(--text-white); letter-spacing: 1px;
  }
  .screen-title {
    position: absolute; left: 239px; top: 136px; width: 195px; height: 51px;
    background: var(--tag-bg); color: var(--text-light);
    font-family: "Tinos", serif; font-size: 32px; line-height: 51px; text-align: center;
  }
  .sender-card {
    position: absolute; left: 52px; top: 234px; width: 571px; height: 237px;
    background: var(--card-bg); border-radius: 24px;
    box-shadow: inset 0 0 12px rgba(0,0,0,.35);
  }
  .sender-photo {
    position: absolute; left: 0; top: 0; width: 237px; height: 237px; border-radius: 20px;
    background: linear-gradient(180deg, #7fb2e0 0%, #a9c8e6 45%, #8e7f8c 75%, #6c6a7a 100%);
    box-shadow: 4px 6px 12px rgba(0,0,0,.6);
  }
  .sender-name {
    position: absolute; left: 248px; top: 22px; font-size: 26px; color: var(--green-text);
  }
  .sender-message {
    position: absolute; left: 248px; top: 80px; width: 240px;
    font-size: 25px; line-height: 31px; color: var(--text-light);
  }
  .topic-list { position: absolute; left: 94px; top: 562px; width: 487px; }
  .topic {
    position: relative; width: 487px; height: 186px; margin-bottom: 20px;
    display: flex; align-items: center; justify-content: center;
  }
  .topic svg { position: absolute; inset: 0; }
  .topic-text {
    position: relative; width: 440px; text-align: center;
    font-size: 22.5px; line-height: 31px; color: var(--text-white);
  }
</style>
</head>
<body>
<main class="screen">
  <header class="app-header">
    <svg width="675" height="150" viewBox="0 0 675 150">
      <defs>
        <linearGradient id="headerGreen" x1="0" y1="0" x2="0" y2="1">
          <stop offset="0" stop-color="var(--green-light)"/>
          <stop offset="1" stop-color="var(--green-dark)"/>
        </linearGradient>
      </defs>
      <path d="M0,0 H675 V106 Q337.5,172 0,106 Z" fill="url(#headerGreen)"/>
    </svg>
    <div class="app-logo">LOGO</div>
  </header>

  <div class="screen-title">Tell a Story</div>

  <section class="sender-card">
    <div class="sender-photo" role="img" aria-label="Profile photo of the friend asking for a story"></div>
    <div class="sender-name">travmoor</div>
    <p class="sender-message">wants to hear a story! Pick a topic.</p>
  </section>

  <section class="topic-list">
    <svg width="0" height="0" style="position:absolute">
      <defs>
        <radialGradient id="topicFill" cx="0.5" cy="0.4" r="0.6">
          <stop offset="0" stop-color="var(--topic-center)"/>
          <stop offset="1" stop-color="var(--topic-edge)"/>
        </radialGradient>
      </defs>
    </svg>
    <div class="topic">
      <svg width="487" height="186" viewBox="0 0 487 186">
        <path d="M20,1 H467 Q486,1 486,20 Q468,93 486,166 Q486,185 467,185 H20 Q1,185 1,166 Q19,93 1,20 Q1,1 20,1Z" fill="url(#topicFill)" stroke="#111" stroke-width="2"/>
        <path d="M4,24 Q22,93 4,162" fill="none" stroke="var(--green-edge)" stroke-width="2"/>
        <path d="M483,24 Q465,93 483,162" fill="none" stroke="var(--green-edge)" stroke-width="2"/>
      </svg>
      <p class="topic-text">Whats is a taste you will never enjoy?</p>
    </div>
    <div class="topic">
      <svg width="487" height="186" viewBox="0 0 487 186">
        <path d="M20,1 H467 Q486,1 486,20 Q468,93 486,166 Q486,185 467,185 H20 Q1,185 1,166 Q19,93 1,20 Q1,1 20,1Z" fill="url(#topicFill)" stroke="#111" stroke-width="2"/>
        <path d="M4,24 Q22,93 4,162" fill="none" stroke="var(--green-edge)" stroke-width="2"/>
        <path d="M483,24 Q465,93 483,162" fill="none" stroke="var(--green-edge)" stroke-width="2"/>
      </svg>
      <p class="topic-text">Would you rathertravel by plane,train, or car?</p>
    </div>
    <div class="topic">
      <svg width="487" height="186" viewBox="0 0 487 186">
        <path d="M20,1 H467 Q486,1 486,20 Q468,93 486,166 Q486,185 467,185 H20 Q1,185 1,166 Q19,93 1,20 Q1,1 20,1Z" fill="url(#topicFill)" stroke="#111" stroke-width="2"/>
        <path d="M4,24 Q22,93 4,162" fill="none" stroke="var(--green-edge)" stroke-width="2"/>
        <path d="M483,24 Q465,93 483,162" fill="none" stroke="var(--green-edge)" stroke-width="2"/>
      </svg>
      <p class="topic-text">If you knew you only had two weeks to live starting today, what would you spend them doing?</p>
    </div>
  </section>
</main>
</body>
</html>
```